Hearing Assessments & Hearing Aids

I need a business card design for my new business called 'Meridale Hearing Aids & Audiometry. I do hearing assessments for adults and children. I also fit hearing aids to hearing impaired people. I would also like to incorporate in my business card Aboriginal designs and colours with a picture of an ear which represents my hearing business as well as my Aboriginal culture.

I would also like my profession added to the business card. I am an Audioetrist.

Target Market(s)

My target customers are everyone concerned with theri hearing and for those who require hearing aids

Industry/Entity Type

Business

Contact Information for Business Card

Meridale Hearing Aids & Audiometry
Tom Harcastle
0432 519 604

Requirements
Must have
• Meridale Hearing Aids & Audiometry
Tom HArcastle
Mobile: 0432 519 604
Email: tomharcastle07@quellnet.com

Audiometrist

```html
<!DOCTYPE html>
<html lang="en">
<head>
<meta charset="utf-8">
<title>Meridale Hearing Aids &amp; Audiometry – Business Card</title>
<link href="https://fonts.googleapis.com/css2?family=Delius&display=swap" rel="stylesheet">
<style>
  :root {
    --backdrop: #c8c8c8;
    --card-gold: #c6a462;
    --ochre-red: #a3241b;
    --earth-brown: #5e4a33;
    --band-tone: #a8804a;
  }
  * { margin: 0; padding: 0; box-sizing: border-box; }
  html, body {
    width: 1200px;
    height: 899px;
    overflow: hidden;
    background: var(--backdrop);
  }
  .card {
    position: absolute;
    left: 398px;
    top: 100px;
    width: 405px;
    height: 700px;
    background: var(--card-gold);
    font-family: "Delius", sans-serif;
  }
  .brand {
    position: absolute;
    right: 163px;
    top: 127px;
    text-align: right;
    color: var(--ochre-red);
    font-size: 24px;
    line-height: 39px;
    text-transform: uppercase;
    letter-spacing: -0.5px;
    white-space: nowrap;
  }
  .brand-dot {
    position: absolute;
    left: 268px;
    top: 188px;
    width: 30px;
    height: 30px;
    border-radius: 50%;
    background: var(--ochre-red);
  }
  .dot-band {
    position: absolute;
    height: 12px;
    border-radius: 6px;
    background: var(--band-tone);
  }
  .dot-band--top { left: 32px; top: 266px; width: 344px; }
  .dot-band--bottom { left: 195px; top: 620px; width: 179px; }
  .person {
    position: absolute;
    right: 33px;
    top: 482px;
    text-align: right;
    white-space: nowrap;
  }
  .person-name {
    color: var(--ochre-red);
    font-size: 40px;
    line-height: 52px;
  }
  .person-role {
    color: var(--earth-brown);
    font-size: 20px;
    line-height: 26px;
  }
  .person-mobile {
    margin-top: 16px;
    color: var(--earth-brown);
    font-size: 22px;
    line-height: 28px;
  }
</style>
</head>
<body>
  <main class="card">
    <div class="brand">Meridale<br>Hearing Aids<br>&amp; Audiometry</div>
    <div class="brand-dot"></div>
    <div class="dot-band dot-band--top" role="img" aria-label="Aboriginal dot-painting border in ochre and brown"></div>
    <section class="person">
      <p class="person-name">Tom Harcastle</p>
      <p class="person-role">Audioetrist</p>
      <p class="person-mobile">Mobile: 0432 519 604</p>
    </section>
    <div class="dot-band dot-band--bottom" role="img" aria-label="Aboriginal dot-painting border in ochre and brown"></div>
  </main>
</body>
</html>
```